ReDesign CBD Packaging Box with needed Details and Pizazzz!

I have 3 things that need to be accomplished for this project to be completed.
1- Each box contains CBD oil in values of 500mg, 1500mg and 2500mg. Each value as a flavor as well. We offer 4 "Flavors": Natural (flavorless), Mint, Dragonfruit and Watermelon in the 3 variants listed above. So need a box for each.
2- After reviewing the design recently, I decided I am not as happy as I thought. So, I am open to any modifications that may make is shine and spark that says "buy me" figuratively.
3- The box should be easy to identify in terms of the amount of CBD and flavor it is. Play with colors maybe where the swirl is white is it is 2500mg, and gray if 1500mg and dark gray for 500mg? Something like that as an example but I am sure you have better ideas than I .

So to summarize, need to update the box with all the wording and information required to be on the box.

I am attaching:
1)the text that should be on the box in case you need it
2) the logo,
3)a version that i tried to making called "dragon fruit tincture 1500mg",
4)the original design packaging called "soapy packaging".
5)the template I am supposed to use.

Target Market(s)

Health and Nutrition, Sports, Alternative Medicine, Elderly,

Industry/Entity Type

Retail online

Requirements
Must have
• clear writing with clear font
Nice to have
• some color or absence of black maybe.
Should not have
• unnecessary images or too busy

```html
<!DOCTYPE html>
<html lang="en">
<head>
<meta charset="utf-8">
<title>Lumen Drops – Full Spectrum CBD Tincture Boxes</title>
<link rel="stylesheet" href="https://fonts.googleapis.com/css2?family=Oswald:wght@300;400;500;700&family=Roboto+Condensed:wght@400;700&display=swap">
<style>
  :root {
    --canvas-bg: #a4a4a4;
    --canvas-bg-light: #c2c2c2;
    --side-bg: #efd9e7;
    --side-ink: #5c5c5c;
    --white: #ffffff;
    --dragon-bg: #e4c0da;
    --dragon-ink: #b35a80;
    --mint-bg: #9fc69b;
    --mint-ink: #1f8a3a;
    --melon-bg: #8fc4c3;
    --melon-ink: #1e6a58;
    --natural-bg: #c9c9c9;
    --natural-ink: #878787;
  }
  * { box-sizing: border-box; margin: 0; padding: 0; }
  html, body { width: 1200px; height: 821px; overflow: hidden; }
  body {
    background: linear-gradient(180deg, var(--canvas-bg-light), var(--canvas-bg));
    font-family: "Oswald", "Roboto Condensed", sans-serif;
  }
  .lineup {
    position: absolute;
    left: 150px; top: 142px;
    display: flex; gap: 14px;
    height: 530px;
  }

  /* Side panel */
  .side-panel {
    width: 150px; height: 100%;
    background: var(--side-bg);
    color: var(--side-ink);
    padding: 14px 10px;
    font-family: "Roboto Condensed", sans-serif;
    font-size: 6px; line-height: 1.35;
    margin-right: -14px;
    box-shadow: inset -8px 0 10px rgba(0,0,0,0.07);
  }
  .side-panel__title { font-size: 9.5px; font-weight: 400; margin-bottom: 6px; }
  .side-panel__block { margin-bottom: 6px; }
  .side-panel__label { font-weight: 700; }
  .nutrition {
    background: var(--white);
    border: 1px solid #999;
    padding: 4px;
    margin: 8px 0;
    font-size: 5px;
  }
  .nutrition__title { font-family: "Oswald", sans-serif; font-weight: 700; font-size: 9px; line-height: 1; color: #444; border-bottom: 2px solid #444; padding-bottom: 2px; margin-bottom: 2px; }
  .nutrition__row { display: flex; justify-content: space-between; border-bottom: 0.5px solid #bbb; padding: 1px 0; }
  .nutrition__row--bold { font-weight: 700; }
  .contact { font-size: 6px; margin-top: 6px; }
  .contact__label { letter-spacing: 0.5px; }

  /* Front panel */
  .box-front {
    position: relative;
    width: 206px; height: 100%;
    background: var(--bg);
    color: var(--ink);
    text-align: center;
    box-shadow: 2px 4px 10px rgba(0,0,0,0.18);
  }
  .box-front--dragonfruit { --bg: var(--dragon-bg); --ink: var(--dragon-ink); }
  .box-front--mint { --bg: var(--mint-bg); --ink: var(--mint-ink); }
  .box-front--watermelon { --bg: var(--melon-bg); --ink: var(--melon-ink); }
  .box-front--natural { --bg: var(--natural-bg); --ink: var(--natural-ink); }

  .frame { position: absolute; inset: 0; width: 206px; height: 530px; }
  .frame__line { fill: none; stroke: var(--ink); stroke-width: 1.4; }
  .frame__line--thin { stroke-width: 0.7; opacity: 0.7; }

  .brand-mark {
    position: absolute; top: 48px; left: 73px;
    width: 60px; height: 60px; border-radius: 50%;
    background: var(--ink);
    box-shadow: 0 0 0 3px var(--bg), 0 0 0 4px var(--ink);
    display: flex; align-items: center; justify-content: center;
  }
  .brand-mark__name { font-weight: 500; font-size: 10px; color: var(--white); letter-spacing: 0.2px; }

  .flavor-art {
    position: absolute; top: 212px; left: 63px; width: 80px; height: 72px;
    border-radius: 50%;
    background: radial-gradient(ellipse, color-mix(in srgb, var(--ink) 55%, transparent) 0%, color-mix(in srgb, var(--ink) 20%, transparent) 55%, transparent 72%);
  }

  .title { position: absolute; top: 136px; left: 0; right: 0; }
  .title__spectrum {
    display: inline-block;
    font-weight: 500; font-size: 12px; letter-spacing: 1.8px; line-height: 1.2;
    border-bottom: 1px solid var(--ink); padding: 0 8px 2px;
  }
  .title__flavor { font-weight: 700; font-size: 25px; line-height: 1; margin-top: 2px; }
  .title__product { font-weight: 500; font-size: 19px; line-height: 1.1; color: var(--white); }

  .strength {
    position: absolute; top: 364px; left: 0; right: 0;
    display: flex; justify-content: center; align-items: flex-end; gap: 8px;
  }
  .strength__figure { display: flex; align-items: flex-end; gap: 2px; }
  .strength__number { font-weight: 500; font-size: 25px; line-height: 0.9; }
  .strength__unit { font-weight: 300; font-size: 10px; line-height: 0.9; text-align: left; }

  .badges { position: absolute; top: 414px; left: 0; right: 0; display: flex; justify-content: center; gap: 16px; }
  .badge {
    width: 44px; height: 44px; border-radius: 50%;
    border: 2px solid var(--white);
    background: radial-gradient(circle, transparent 58%, var(--white) 60%, var(--white) 64%, transparent 66%);
  }

  .certified {
    position: absolute; top: 466px; left: 50%; transform: translateX(-50%);
    background: var(--white); color: var(--ink);
    font-weight: 500; font-size: 8.5px; letter-spacing: 0.3px; white-space: nowrap;
    padding: 2px 6px; border-radius: 3px;
  }
  .volume {
    position: absolute; top: 504px; left: 0; right: 0;
    color: var(--white); font-weight: 300; font-size: 11px; letter-spacing: 0.3px;
  }
</style>
</head>
<body>
<main class="lineup">

  <section class="side-panel">
    <h2 class="side-panel__title">Dragon Fruit Tincture</h2>
    <p class="side-panel__block"><span class="side-panel__label">INGREDIENTS:</span> Organic Non-GMP Coconut Oil, Certified Vegan and Highest Quality Full Spectrum CBD, Natural Vegan Flavoring.</p>
    <p class="side-panel__block"><span class="side-panel__label">DIRECTIONS:</span> Recommended dosage is 0.25mg CBD multiplied by your body weight in pounds on a daily basis.</p>
    <p class="side-panel__block"><span class="side-panel__label">WARNINGS:</span> Contains Tree Nuts (Coconut). Consult your doctor before use. Discontinue use if any adverse reactions occur. Do not use if tamper seal is broken.</p>
    <div class="nutrition">
      <div class="nutrition__title">Nutrition Facts<br>Valeur Nutritive</div>
      <div class="nutrition__row"><span>Serving Size 1 tbsp (8 g) / Portion 1 c. à soupe</span></div>
      <div class="nutrition__row nutrition__row--bold"><span>Calories / Calories 30</span></div>
      <div class="nutrition__row"><span>Total Fat / Lipides 1 g</span><span>2%</span></div>
      <div class="nutrition__row"><span>Saturated / Saturés 0 g</span><span>0%</span></div>
      <div class="nutrition__row"><span>Cholesterol / Cholestérol 0 mg</span><span>0%</span></div>
      <div class="nutrition__row"><span>Sodium / Sodium 800 mg</span><span>33%</span></div>
      <div class="nutrition__row"><span>Total Carbohydrate / Glucides 5 g</span><span>2%</span></div>
      <div class="nutrition__row"><span>Protein / Protéines 1 g</span><span></span></div>
    </div>
    <div class="contact">
      <p class="contact__label">CONTACT:</p>
      <p>LUMEN DROPS</p>
      <p>Harbor Vale, CA 90000</p>
      <p>(800) 555-0142</p>
      <p>lumendrops.example</p>
    </div>
  </section>

  <article class="box-front box-front--dragonfruit">
    <svg class="frame" viewBox="0 0 206 530" aria-hidden="true">
      <path class="frame__line" d="M12 206 V40 Q103 -8 194 40 V206"/>
      <path class="frame__line frame__line--thin" d="M18 200 V44 Q103 0 188 44 V200"/>
      <path class="frame__line" d="M26 132 Q26 72 103 40 Q180 72 180 132"/>
      <path class="frame__line" d="M12 196 V322 Q103 350 194 322 V196"/>
      <path class="frame__line frame__line--thin" d="M18 202 V316 Q103 342 188 316 V202"/>
      <path class="frame__line" d="M30 206 Q103 300 176 206"/>
      <path class="frame__line frame__line--thin" d="M60 250 Q103 236 146 250"/>
    </svg>
    <div class="brand-mark"><span class="brand-mark__name">Lumen Drops</span></div>
    <div class="flavor-art" role="img" aria-label="Line drawing of a dragon fruit flower"></div>
    <div class="title">
      <span class="title__spectrum">FULL SPECTRUM</span>
      <h1 class="title__flavor">DRAGONFRUIT</h1>
      <p class="title__product">CBD TINCTURE</p>
    </div>
    <div class="strength">
      <div class="strength__figure"><span class="strength__number">2500</span><span class="strength__unit">MG<br>CBD</span></div>
      <div class="strength__figure"><span class="strength__number">45</span><span class="strength__unit">MG CBD<br>PER ML</span></div>
    </div>
    <div class="badges"><span class="badge"></span><span class="badge"></span></div>
    <p class="certified">ALL NATURAL AND VEGAN CERTIFIED</p>
    <p class="volume">2 fl oz. 59.1471 mL</p>
  </article>

  <article class="box-front box-front--mint">
    <svg class="frame" viewBox="0 0 206 530" aria-hidden="true">
      <path class="frame__line" d="M12 206 V40 Q103 -8 194 40 V206"/>
      <path class="frame__line frame__line--thin" d="M18 200 V44 Q103 0 188 44 V200"/>
      <path class="frame__line" d="M26 132 Q26 72 103 40 Q180 72 180 132"/>
      <path class="frame__line" d="M12 196 V322 Q103 350 194 322 V196"/>
      <path class="frame__line frame__line--thin" d="M18 202 V316 Q103 342 188 316 V202"/>
      <path class="frame__line" d="M30 206 Q103 300 176 206"/>
      <path class="frame__line frame__line--thin" d="M60 250 Q103 236 146 250"/>
    </svg>
    <div class="brand-mark"><span class="brand-mark__name">Lumen Drops</span></div>
    <div class="flavor-art" role="img" aria-label="Line drawing of mint leaves"></div>
    <div class="title">
      <span class="title__spectrum">FULL SPECTRUM</span>
      <h1 class="title__flavor">MINT</h1>
      <p class="title__product">CBD TINCTURE</p>
    </div>
    <div class="strength">
      <div class="strength__figure"><span class="strength__number">2500</span><span class="strength__unit">MG<br>CBD</span></div>
      <div class="strength__figure"><span class="strength__number">45</span><span class="strength__unit">MG CBD<br>PER ML</span></div>
    </div>
    <div class="badges"><span class="badge"></span><span class="badge"></span></div>
    <p class="certified">ALL NATURAL AND VEGAN CERTIFIED</p>
    <p class="volume">2 fl oz. 59.1471 mL</p>
  </article>

  <article class="box-front box-front--watermelon">
    <svg class="frame" viewBox="0 0 206 530" aria-hidden="true">
      <path class="frame__line" d="M12 206 V40 Q103 -8 194 40 V206"/>
      <path class="frame__line frame__line--thin" d="M18 200 V44 Q103 0 188 44 V200"/>
      <path class="frame__line" d="M26 132 Q26 72 103 40 Q180 72 180 132"/>
      <path class="frame__line" d="M12 196 V322 Q103 350 194 322 V196"/>
      <path class="frame__line frame__line--thin" d="M18 202 V316 Q103 342 188 316 V202"/>
      <path class="frame__line" d="M30 206 Q103 300 176 206"/>
      <path class="frame__line frame__line--thin" d="M60 250 Q103 236 146 250"/>
    </svg>
    <div class="brand-mark"><span class="brand-mark__name">Lumen Drops</span></div>
    <div class="flavor-art" role="img" aria-label="Line drawing of a watermelon"></div>
    <div class="title">
      <span class="title__spectrum">FULL SPECTRUM</span>
      <h1 class="title__flavor">WATERMELON</h1>
      <p class="title__product">CBD TINCTURE</p>
    </div>
    <div class="strength">
      <div class="strength__figure"><span class="strength__number">2500</span><span class="strength__unit">MG<br>CBD</span></div>
      <div class="strength__figure"><span class="strength__number">45</span><span class="strength__unit">MG CBD<br>PER ML</span></div>
    </div>
    <div class="badges"><span class="badge"></span><span class="badge"></span></div>
    <p class="certified">ALL NATURAL AND VEGAN CERTIFIED</p>
    <p class="volume">2 fl oz. 59.1471 mL</p>
  </article>

  <article class="box-front box-front--natural">
    <svg class="frame" viewBox="0 0 206 530" aria-hidden="true">
      <path class="frame__line" d="M12 206 V40 Q103 -8 194 40 V206"/>
      <path class="frame__line frame__line--thin" d="M18 200 V44 Q103 0 188 44 V200"/>
      <path class="frame__line" d="M26 132 Q26 72 103 40 Q180 72 180 132"/>
      <path class="frame__line" d="M12 196 V322 Q103 350 194 322 V196"/>
      <path class="frame__line frame__line--thin" d="M18 202 V316 Q103 342 188 316 V202"/>
      <path class="frame__line" d="M30 206 Q103 300 176 206"/>
      <path class="frame__line frame__line--thin" d="M60 250 Q103 236 146 250"/>
    </svg>
    <div class="brand-mark"><span class="brand-mark__name">Lumen Drops</span></div>
    <div class="flavor-art" role="img" aria-label="Line drawing of a tree"></div>
    <div class="title">
      <span class="title__spectrum">FULL SPECTRUM</span>
      <h1 class="title__flavor">NATURAL</h1>
      <p class="title__product">CBD TINCTURE</p>
    </div>
    <div class="strength">
      <div class="strength__figure"><span class="strength__number">2500</span><span class="strength__unit">MG<br>CBD</span></div>
      <div class="strength__figure"><span class="strength__number">45</span><span class="strength__unit">MG CBD<br>PER ML</span></div>
    </div>
    <div class="badges"><span class="badge"></span><span class="badge"></span></div>
    <p class="certified">ALL NATURAL AND VEGAN CERTIFIED</p>
    <p class="volume">2 fl oz. 59.1471 mL</p>
  </article>

</main>
</body>
</html>
```